Brookvale Health Solutions

I need a professional and informational website for healthcare professionals. Please make the website the same style and content as our attached pdf.

Target Market(s)

Medical doctors

Industry/Entity Type

Healthcare

Coding

Coded - Design and coding required

Number of Pages Required

4 page

Requirements
Must have
• The same style and content as the uploaded powerpoints

```html
<!DOCTYPE html>
<html lang="en">
<head>
<meta charset="utf-8">
<title>Brookvale Health Solutions</title>
<link href="https://fonts.googleapis.com/css2?family=Inter:wght@400;500;600;700&family=Plus+Jakarta+Sans:wght@600;700;800&display=swap" rel="stylesheet">
<style>
:root{
  --ink:#0b1120;
  --navy-deep:#030b1e;
  --navy:#0a2448;
  --teal:#1f6f6b;
  --teal-bright:#7fd4cf;
  --teal-soft:#e3f4f2;
  --text:#3c4656;
  --muted:#6b7585;
  --light:#f6f7f9;
  --grey:#eef0f1;
  --line:#e3e6ea;
  --white:#fff;
}
*{margin:0;padding:0;box-sizing:border-box}
html,body{width:1200px;height:2947px;overflow:hidden;background:var(--white)}
body{font-family:'Inter',sans-serif;color:var(--text);position:relative}
.head{font-family:'Plus Jakarta Sans',sans-serif;color:var(--ink);letter-spacing:-.02em}
.abs{position:absolute}

/* nav */
.nav{position:absolute;left:0;top:0;width:1200px;height:73px;background:var(--white)}
.brand{position:absolute;left:41px;top:14px;line-height:1}
.brand b{display:block;font-family:'Plus Jakarta Sans',sans-serif;font-weight:800;font-size:27px;color:var(--ink);letter-spacing:-.01em}
.brand span{display:block;font-size:11px;color:var(--ink);margin-top:2px;padding-left:28px}
.nav-links{position:absolute;left:447px;top:29px;display:flex;gap:28px;font-size:13px;color:#3c4656}
.nav-links a{color:inherit;text-decoration:none}
.nav-links .active{color:var(--teal);border-bottom:2px solid var(--teal);padding-bottom:6px}
.btn-contact{position:absolute;left:1062px;top:19px;width:97px;height:36px;background:var(--ink);color:#fff;font-size:13px;font-weight:600;display:flex;align-items:center;justify-content:center;border-radius:2px}

/* hero */
.hero{position:absolute;left:0;top:73px;width:1200px;height:695px;background:linear-gradient(160deg,#020817 0%,#030d24 60%,#062454 100%)}
.pill{position:absolute;left:41px;top:164px;height:23px;padding:0 12px;border:1px solid #17403f;border-radius:12px;background:#071a22;color:#3d9c95;font-size:11px;font-weight:600;letter-spacing:.12em;display:flex;align-items:center;gap:7px}
.pill i{width:6px;height:6px;border-radius:50%;background:#3d9c95}
.hero h1{position:absolute;left:41px;top:206px;font-family:'Plus Jakarta Sans',sans-serif;font-weight:800;font-size:68px;line-height:65px;color:#fff;letter-spacing:-.035em}
.hero h1 em{font-style:normal;background:linear-gradient(90deg,#86dcd5,#2f8c87);-webkit-background-clip:text;background-clip:text;color:transparent}
.hero p{position:absolute;left:41px;top:368px;width:530px;font-size:19px;line-height:26px;color:#8494ab}
.btn-primary{position:absolute;left:41px;top:481px;width:197px;height:52px;background:var(--teal);color:#fff;font-weight:600;font-size:15px;display:flex;align-items:center;justify-content:center;gap:8px;border-radius:2px;box-shadow:0 8px 20px rgba(31,111,107,.35)}
.btn-ghost{position:absolute;left:252px;top:481px;width:191px;height:52px;border:1px solid #1d2a40;background:#050e22;color:#fff;font-weight:600;font-size:15px;display:flex;align-items:center;justify-content:center;border-radius:2px}
.portrait{position:absolute;left:719px;top:74px;width:439px;height:548px;border-radius:8px;background:radial-gradient(ellipse at 50% 60%,#4aa8a4 0%,#2c8a86 55%,#1f6f6b 100%);border:1px solid #2d5a68}
.stat-card{position:absolute;left:697px;top:510px;width:218px;height:135px;background:#fff;border-radius:6px;box-shadow:0 14px 32px rgba(0,0,0,.35)}
.stat-icon{position:absolute;left:22px;top:34px;width:30px;height:30px;border-radius:4px;background:var(--teal-soft);display:flex;align-items:center;justify-content:center}
.stat-card small{position:absolute;left:69px;top:25px;font-size:8px;color:#8a93a2;letter-spacing:.02em}
.stat-card h4{position:absolute;left:69px;top:38px;font-size:13px;line-height:18px;font-weight:600;color:var(--ink)}
.stat-bar{position:absolute;left:22px;top:83px;width:170px;height:6px;border-radius:3px;background:var(--teal)}
.stat-card .rate{position:absolute;left:22px;top:99px;font-size:10px;color:#6b7585}

/* solutions */
.solutions{position:absolute;left:0;top:768px;width:1200px;height:895px;background:var(--light)}
.eyebrow{font-size:12px;font-weight:700;letter-spacing:.25em;color:var(--teal)}
.card{position:absolute;background:#fff;border-radius:4px;box-shadow:0 1px 2px rgba(0,0,0,.03)}
.card h3{font-family:'Plus Jakarta Sans',sans-serif;font-weight:700;color:var(--ink);letter-spacing:-.01em}
.tag{display:inline-block;font-size:10px;font-weight:700;letter-spacing:.06em;padding:6px 11px;border-radius:2px;margin-right:12px}

/* partner */
.partner{position:absolute;left:0;top:1663px;width:1200px;height:618px;background:linear-gradient(180deg,#0a2248,#072452)}
.feature{position:absolute;left:41px;width:520px}
.feature .ico{position:absolute;left:0;top:0;width:45px;height:45px;border:1px solid #1f4a66;background:#0f3050;display:flex;align-items:center;justify-content:center;border-radius:2px}
.feature h4{position:absolute;left:66px;top:0;font-size:17px;font-weight:600;color:#fff}
.feature p{position:absolute;left:66px;top:28px;width:450px;font-size:12.5px;line-height:21px;color:#7488a6}
.quote-card{position:absolute;left:637px;top:87px;width:521px;height:444px;border:1px solid #1f3d64;border-radius:10px;background:linear-gradient(160deg,#143257,#0b2a52)}

/* newsletter */
.news{position:absolute;left:0;top:2281px;width:1200px;height:339px;background:#f3f4f6;text-align:center}

/* footer */
.footer{position:absolute;left:0;top:2620px;width:1200px;height:327px;background:#fff}
.fcol{position:absolute;top:53px}
.fcol h5{font-size:13px;font-weight:600;letter-spacing:.18em;color:var(--ink);margin-bottom:20px}
.fcol li{list-style:none;font-size:11px;color:#3c4656;margin-bottom:15px;display:flex;align-items:center;gap:6px}
</style>
</head>
<body>

<header class="nav">
  <div class="brand"><b>BROOKVALE</b><span>Health Solutions</span></div>
  <nav class="nav-links">
    <a class="active">Home</a><a>Clinical Solutions</a><a>Patient Records</a><a>About Us</a>
  </nav>
  <div class="btn-contact">Contact</div>
</header>

<section class="hero">
  <div class="pill"><i></i>PRECISION MEDICAL INTELLIGENCE</div>
  <h1>Innovative Care for<br><em>Modern Medicine</em></h1>
  <p>Brookvale Health Solutions provides specialized data-driven frameworks for medical professionals who demand surgical precision in clinical workflows.</p>
  <div class="btn-primary">Explore Solutions
    <svg width="10" height="10" viewBox="0 0 10 10"><path d="M1 5h7M5 2l3 3-3 3" stroke="#fff" stroke-width="1.3" fill="none"/></svg></div>
  <div class="btn-ghost">View Case Studies</div>
  <div class="portrait" role="img" aria-label="Portrait of a physician in a white coat with a stethoscope on a teal backdrop"></div>
  <div class="stat-card">
    <div class="stat-icon"><svg width="14" height="14" viewBox="0 0 14 14" fill="none" stroke="#1f6f6b" stroke-width="1.3"><rect x="1" y="1" width="12" height="12" rx="1"/><path d="M4 10V8M7 10V5M10 10V7"/></svg></div>
    <small>REAL-TIME STATS</small>
    <h4>Diagnostic<br>Accuracy</h4>
    <div class="stat-bar"></div>
    <div class="rate">98.4% Precision Rating</div>
  </div>
</section>

<section class="solutions">
  <div class="eyebrow abs" style="left:41px;top:89px">THE CLINICAL STACK</div>
  <h2 class="head abs" style="left:41px;top:116px;font-size:36px;font-weight:700">Core Clinical Solutions</h2>

  <div class="card" style="left:42px;top:211px;width:737px;height:297px">
    <svg class="abs" style="left:35px;top:35px" width="22" height="28" viewBox="0 0 22 28" fill="none" stroke="#1f6f6b" stroke-width="2"><path d="M4 26h14M8 22h8M11 22c5 0 7-4 6-8M9 3l4 2-4 9-4-2zM6 14l-2 4"/></svg>
    <h3 class="abs" style="left:36px;top:97px;font-size:22px">Predictive Patient Diagnostics</h3>
    <p class="abs" style="left:36px;top:138px;width:520px;font-size:14.5px;line-height:24px">Leverage high-fidelity AI models trained on millions of clinical markers to identify patient risks before they manifest symptomatically. Built for specialized oncology and cardiology workflows.</p>
    <div class="abs" style="left:36px;top:236px">
      <span class="tag" style="background:var(--teal-soft);color:var(--teal)">AI POWERED</span><span class="tag" style="background:#eef0f2;color:#4a5262">ONCOLOGY</span>
    </div>
  </div>

  <div class="card" style="left:801px;top:211px;width:357px;height:224px;background:var(--navy-deep)">
    <svg class="abs" style="left:30px;top:30px" width="22" height="22" viewBox="0 0 22 22" fill="none" stroke="#7fd4cf" stroke-width="1.8"><rect x="2" y="3" width="18" height="17" rx="2"/><path d="M7 1v4M15 1v4"/><circle cx="11" cy="10" r="2.5"/><path d="M6 17c1-3 9-3 10 0"/></svg>
    <h3 class="abs" style="left:30px;top:80px;font-size:19px;color:#fff">Seamless EHR Sync</h3>
    <p class="abs" style="left:30px;top:113px;width:300px;font-size:12.5px;line-height:21px;color:#8794a8">Unified interoperability across legacy systems without compromising security or data integrity.</p>
    <div class="abs" style="left:30px;top:177px;font-size:12.5px;font-weight:600;color:var(--teal-bright)">Learn More &nbsp;→</div>
  </div>

  <div class="card" style="left:42px;top:532px;width:356px;height:208px">
    <svg class="abs" style="left:30px;top:29px" width="24" height="20" viewBox="0 0 24 20" fill="none" stroke="#1f6f6b" stroke-width="1.8"><rect x="1" y="1" width="22" height="18" rx="2"/><path d="M1 10h6l2-4 3 8 2-4h9"/></svg>
    <h3 class="abs" style="left:30px;top:78px;font-size:19px">Remote Bio-Monitoring</h3>
    <p class="abs" style="left:30px;top:109px;width:310px;font-size:12.5px;line-height:21px">Continuous telemetry streams direct to your dashboard with smart alerting for vital deviations.</p>
    <div class="abs" style="left:30px;top:174px;width:30px;height:3px;background:var(--teal);border-radius:2px"></div>
    <div class="abs" style="left:64px;top:174px;width:6px;height:3px;background:#dde1e5;border-radius:2px"></div>
    <div class="abs" style="left:74px;top:174px;width:6px;height:3px;background:#dde1e5;border-radius:2px"></div>
  </div>

  <div class="card" style="left:421px;top:531px;width:737px;height:277px;background:var(--grey);box-shadow:none">
    <div class="abs" style="left:31px;top:35px;width:215px;height:206px;background:#fff;display:flex;align-items:center;justify-content:center">
      <svg width="38" height="46" viewBox="0 0 38 46"><path d="M19 2 3 8v14c0 11 7 19 16 22 9-3 16-11 16-22V8z" fill="#e6e9ee" stroke="#c9ced6" stroke-width="2"/><path d="M19 2v42c9-3 16-11 16-22V8z" fill="#c9ced6"/></svg>
    </div>
    <h3 class="abs" style="left:276px;top:70px;font-size:19px">Enterprise Grade Security</h3>
    <p class="abs" style="left:276px;top:101px;width:430px;font-size:12.5px;line-height:21px">HIPAA, SOC2, and GDPR compliant by design. Our "Clinical Atelier" approach ensures that data privacy is an architectural foundation, not an afterthought.</p>
    <div class="abs" style="left:276px;top:183px;display:flex">
      <span style="width:28px;height:28px;border-radius:50%;background:#eef0f3;border:2px solid #fff"></span>
      <span style="width:28px;height:28px;border-radius:50%;background:#d7dde5;border:2px solid #fff;margin-left:-6px"></span>
      <span style="width:28px;height:28px;border-radius:50%;background:#b8c2cf;border:2px solid #fff;margin-left:-6px"></span>
    </div>
    <div class="abs" style="left:363px;top:192px;font-size:9.5px;font-weight:700;color:#556070">TRUSTED BY 150+ HOSPITALS</div>
  </div>
</section>

<section class="partner">
  <h2 class="head abs" style="left:41px;top:120px;font-size:46px;font-weight:800;color:#fff">Why Partner with Us?</h2>
  <div class="feature" style="top:198px">
    <div class="ico"><svg width="16" height="18" viewBox="0 0 16 18" fill="none" stroke="#7fd4cf" stroke-width="1.6"><path d="M8 1 2 3.5v5C2 13 5 16 8 17c3-1 6-4 6-8.5v-5z"/><path d="m5 9 2 2 4-4"/></svg></div>
    <h4>Physician-First Philosophy</h4>
    <p>We design for the expert user. No over-simplified buttons; only functional, high-density interfaces built for clinical speed.</p>
  </div>
  <div class="feature" style="top:308px">
    <div class="ico"><svg width="18" height="18" viewBox="0 0 18 18" fill="none" stroke="#7fd4cf" stroke-width="1.6"><circle cx="9" cy="9" r="7.5"/><path d="m9 10 4-4M5 12h0"/></svg></div>
    <h4>Reduced Cognitive Load</h4>
    <p>Our asymmetric precision layouts reduce visual fatigue, allowing for longer focus periods during intensive chart reviews.</p>
  </div>
  <div class="feature" style="top:418px">
    <div class="ico"><svg width="20" height="20" viewBox="0 0 20 20" fill="none" stroke="#7fd4cf" stroke-width="1.5"><circle cx="10" cy="10" r="2.5"/><circle cx="10" cy="2.5" r="1.6"/><circle cx="10" cy="17.5" r="1.6"/><circle cx="2.5" cy="6" r="1.6"/><circle cx="17.5" cy="6" r="1.6"/><circle cx="2.5" cy="14" r="1.6"/><circle cx="17.5" cy="14" r="1.6"/><path d="M10 4v3.5M10 12.5V16M4 7l4 2M16 7l-4 2M4 13l4-2M16 13l-4-2"/></svg></div>
    <h4>Agile Integration</h4>
    <p>Implementation cycles that respect your clinic's uptime. We deploy in weeks, not quarters.</p>
  </div>

  <div class="quote-card">
    <div class="abs" role="img" aria-label="Headshot of the chief medical officer" style="left:30px;top:30px;width:57px;height:57px;border-radius:8px;background:linear-gradient(160deg,#5fb3ae,#2c8a86);border:2px solid #3b8c88"></div>
    <div class="abs" style="left:102px;top:44px;font-size:15px;font-weight:600;color:#fff">Dr. Elena Marsh</div>
    <div class="abs" style="left:102px;top:64px;font-size:11px;font-weight:600;letter-spacing:.12em;color:var(--teal-bright)">CHIEF MEDICAL OFFICER</div>
    <div class="abs" style="left:32px;top:118px;font-family:Georgia,serif;font-size:34px;font-weight:700;color:#1f5a6a">”</div>
    <p class="abs" style="left:30px;top:162px;width:460px;font-size:19px;line-height:29.5px;color:#fff">"Brookvale Health Solutions transformed our oncology unit from a reactive practice to a predictive powerhouse. The interface is remarkably sophisticated—it actually feels like it was designed by people who understand the stakes of a clinical environment."</p>
    <div class="abs" style="left:30px;top:372px;width:461px;height:1px;background:#24456b"></div>
    <div class="abs" style="left:30px;top:394px;font-size:11px;letter-spacing:3px;color:#2f6d7e">☆☆☆☆☆</div>
    <div class="abs" style="left:380px;top:396px;width:111px;text-align:right;font-size:11px;font-weight:600;letter-spacing:.12em;color:#5b7696">CASE STUDY #412</div>
  </div>
</section>

<section class="news">
  <h2 class="head" style="margin-top:77px;font-size:29px;font-weight:700">Stay Informed on Clinical Innovation</h2>
  <p style="margin:22px auto 0;width:480px;font-size:14.5px;line-height:22px">Receive our quarterly journal on AI in medicine and clinical workflow optimization. No fluff, just technical excellence.</p>
  <div class="abs" style="left:369px;top:209px;width:323px;height:41px;background:#fff;border:1px solid var(--line);font-size:13px;color:#7a8494;padding-left:14px;display:flex;align-items:center">Medical Email Address</div>
  <div class="abs" style="left:703px;top:208px;width:129px;height:43px;background:var(--ink);color:#fff;font-size:15px;font-weight:600;display:flex;align-items:center;justify-content:center;box-shadow:0 6px 14px rgba(0,0,0,.18)">Subscribe</div>
</section>

<footer class="footer">
  <div class="abs" style="left:41px;top:42px;line-height:1">
    <div style="font-family:'Plus Jakarta Sans',sans-serif;font-weight:800;font-size:19px;color:var(--ink)">BROOKVALE</div>
    <div style="font-size:7px;color:var(--ink);padding-left:19px;margin-top:1px">Health Solutions</div>
  </div>
  <p class="abs" style="left:41px;top:98px;width:260px;font-size:11px;line-height:18px;color:#6b7585">Dedicated to advancing the frontiers of modern medicine through precision data frameworks and clinical intelligence.</p>

  <div class="fcol" style="left:332px"><h5>SOLUTIONS</h5><ul><li>Oncology Analytics</li><li>Cardiology Suite</li><li>EHR Integration</li><li>Remote Monitoring</li></ul></div>
  <div class="fcol" style="left:622px"><h5>ORGANIZATION</h5><ul><li>Our Philosophy</li><li>Security Standards</li><li>Clinical Research</li><li>Partner Network</li></ul></div>
  <div class="fcol" style="left:913px"><h5>CONTACT</h5><ul>
    <li><svg width="10" height="8" viewBox="0 0 10 8" fill="none" stroke="#3c4656"><rect x=".5" y=".5" width="9" height="7"/><path d="m.5 .5 4.5 4 4.5-4"/></svg>info@brookvalehealth.io</li>
    <li><svg width="10" height="10" viewBox="0 0 10 10" fill="none" stroke="#3c4656"><path d="M1.5 1h2l1 2.5-1.3 1a6 6 0 0 0 2.3 2.3l1-1.3 2.5 1v2A1 1 0 0 1 8 9.5 7.5 7.5 0 0 1 .5 2 1 1 0 0 1 1.5 1z"/></svg>+1 (800) 555-0142</li>
    <li><svg width="9" height="11" viewBox="0 0 9 11" fill="none" stroke="#3c4656"><path d="M4.5 10S1 6.5 1 4.3a3.5 3.5 0 0 1 7 0C8 6.5 4.5 10 4.5 10z"/><circle cx="4.5" cy="4.3" r="1.2"/></svg>San Francisco, CA</li>
  </ul></div>

  <div class="abs" style="left:0;top:260px;width:1200px;text-align:center;font-size:9.5px;font-weight:600;letter-spacing:.12em;color:#8a93a2;line-height:15px">© 2024 BROOKVALE HEALTH SOLUTIONS. ALL RIGHTS RESERVED.<br>PRIVACY POLICY &nbsp;&nbsp;&nbsp;&nbsp; TERMS OF SERVICE</div>
</footer>

</body>
</html>
```